Varnel Flyer

We need a flyer designed for a Security Company. Our main focus is security consulting and risk management. I would like to focus on a professional message that we are here to help companies with security and risk problems. We are independent and do not affiliate with any other companies.

Who we are:
Over 25+ years of experience in Security and Law Enforcement
Specialize in Security Management
Board Certified in Security management
Accredited defense Specialist (ADS)
We are not affiliated with any security provider or guard company we provide independent advise

Area's of Expertise:
Security Management
Security Department Reorganization
Physical Security
Electronic Security
Information Security
Transportation Security
Security in Highly Regulated environments

Services Offered:

Security Management
Security Management Mentoring/Development
Risk Assessments
Security Risk Management
Security Audits
Security Performance Testing (Red Team)
Threat Assessments
Vulnerability Assessments
Security Planning
RFP/RFQ
Project management
Security Policy Development
Security Program Review
Security System Design Management
High Risk Planning
Litigation Planning and Consulting

What to look for in a Security Consultant:

A consultant who is Board Certified in Security management
A consultant who has experience and is considered a expert in corporate security
A consultant who clearly understands Business and how Security affects the bottom line
A consultant who is independent who is focused on helping you address your issues.
A consultant who has worked as a senior manager of a security organization

Industries:

Energy
Healthcare
Real Estate
Nuclear
Highly secure facilities

Accredited Defense Specialist (ADS)

The Accredited Defense Specialist (ADSⓇ) is considered the “gold standard” certification for security management professionals and demonstrates knowledge and competency in seven key domains of security. Globally recognized as the standard of excellence for security management professionals. The ADS is administered by OPRA Worldwide, which is the predominant international organization for security Internationally.

Contact us:

Phone: 555-271-6043
info@varnelguard.example
www.varnelguard.example

```html
<!DOCTYPE html>
<html lang="en">
<head>
<meta charset="utf-8">
<title>Varnel Services – Security Consulting Flyer</title>
<link rel="stylesheet" href="https://fonts.googleapis.com/css2?family=Alegreya+Sans+SC:wght@300;400&family=Raleway:wght@500&display=swap">
<style>
  :root {
    --page: #ffffff;
    --panel: #151515;
    --ink: #f2f2f2;
    --ink-soft: #d9d9d9;
    --rule: #bdbdbd;
    --band: #c9c9c9;
    --band-ink: #111111;
    --brand: #1f4f9a;
    --badge: #b9b9b9;
  }
  * { box-sizing: border-box; margin: 0; padding: 0; }
  html, body { width: 1000px; height: 1200px; overflow: hidden; background: var(--page); }
  body { position: relative; font-family: "Alegreya Sans SC", sans-serif; font-weight: 300; color: var(--ink); }

  .flyer {
    position: absolute; left: 86px; top: 22px; width: 828px; height: 1156px;
    background: var(--panel); overflow: hidden;
  }
  .abs { position: absolute; }

  .hero-visual {
    left: 4px; top: 68px; width: 470px; height: 380px;
    background: radial-gradient(ellipse 46% 50% at 55% 45%, #9a9a9a 0%, #555 30%, #262626 62%, var(--panel) 100%);
  }

  .brand { left: 612px; top: 44px; display: flex; align-items: center; gap: 10px; }
  .brand-mark { width: 42px; height: 42px; border-radius: 50%; background: var(--brand); }
  .brand-name { font-size: 27px; font-weight: 400; color: var(--brand); letter-spacing: 2px; line-height: 1; }
  .brand-tag { left: 668px; top: 93px; font-size: 8px; color: var(--ink-soft); letter-spacing: .5px; }

  .rule { border-top: 1px dashed var(--rule); height: 0; }

  .industries { left: 514px; top: 150px; }
  .industries h2 { font-weight: 300; font-size: 38px; letter-spacing: .5px; margin-bottom: 6px; }
  .industry-list { list-style: none; }
  .industry-list li { display: flex; align-items: flex-start; font-size: 27px; line-height: 34px; letter-spacing: 1.5px; }
  .industry-list svg { width: 22px; height: 22px; margin: 6px 21px 0 8px; flex: none; fill: var(--ink); }

  .criteria-title { left: 36px; top: 458px; display: flex; align-items: center; gap: 16px; }
  .criteria-title svg { width: 36px; height: 36px; fill: var(--ink); }
  .criteria-title h2 { font-weight: 300; font-size: 31px; letter-spacing: .8px; }

  .criterion { display: flex; gap: 8px; width: 182px; font-size: 13.5px; line-height: 22.7px; letter-spacing: .4px; color: var(--ink-soft); }
  .criterion svg { width: 24px; height: 28px; flex: none; margin-top: -1px; }

  .cert-copy { left: 32px; top: 812px; width: 440px; }
  .cert-copy h3 { font-weight: 300; font-size: 23px; letter-spacing: .4px; margin-bottom: 2px; }
  .cert-copy p { font-size: 13.2px; line-height: 18.6px; letter-spacing: .4px; color: var(--ink-soft); }

  .cert-badge { left: 520px; top: 815px; width: 274px; height: 90px; border-radius: 45px 8px 8px 45px; background: var(--badge); }

  .contact-title { left: 55px; top: 1024px; font-family: "Raleway", sans-serif; font-weight: 500; font-size: 30px; letter-spacing: .5px; }
  .contact-band {
    left: 0; top: 1070px; width: 828px; height: 40px; background: var(--band);
    display: flex; align-items: center; padding-left: 48px;
    font-family: "Raleway", sans-serif; font-weight: 500; font-size: 19px; color: var(--band-ink);
  }
  .contact-item { display: flex; align-items: center; gap: 12px; }
  .contact-item svg { width: 26px; height: 26px; }
  .contact-item + .contact-item { margin-left: 34px; }
</style>
</head>
<body>
<main class="flyer">
  <div class="abs hero-visual" role="img" aria-label="Close-up of a human eye overlaid with a digital iris-scan targeting interface"></div>

  <div class="abs brand">
    <span class="brand-mark"></span>
    <span class="brand-name">Varnel Services</span>
  </div>
  <div class="abs brand-tag">a Security Management Company</div>

  <div class="abs rule" style="left:471px;top:140px;width:340px"></div>

  <section class="abs industries">
    <h2>Industries</h2>
    <ul class="industry-list">
      <li><svg viewBox="0 0 24 24"><path d="M14 1 5 14h6l-2 9 9-14h-6z"/></svg>Energy</li>
      <li><svg viewBox="0 0 24 24"><path d="M1 8h14v11H1zM15 11h5l3 4v4h-8z"/><path fill="#151515" d="M7 10h2v3h3v2H9v3H7v-3H4v-2h3z"/><circle cx="5" cy="20" r="2.5"/><circle cx="18" cy="20" r="2.5"/></svg>Healthcare</li>
      <li><svg viewBox="0 0 24 24"><path d="M12 2 1 12h3v10h6v-6h4v6h6V12h3z"/></svg>Real Estate</li>
      <li><svg viewBox="0 0 24 24" fill="none" stroke="#f2f2f2" stroke-width="1.4"><ellipse cx="12" cy="12" rx="11" ry="4.2"/><ellipse cx="12" cy="12" rx="11" ry="4.2" transform="rotate(60 12 12)"/><ellipse cx="12" cy="12" rx="11" ry="4.2" transform="rotate(-60 12 12)"/><circle cx="12" cy="12" r="1.8" fill="#f2f2f2"/></svg>Nuclear</li>
      <li><svg viewBox="0 0 24 24"><circle cx="12" cy="8" r="5"/><path d="M3 23c0-6 4-9 9-9s9 3 9 9z"/></svg>Highly secure<br>facilities</li>
    </ul>
  </section>

  <div class="abs rule" style="left:467px;top:425px;width:340px"></div>

  <div class="abs criteria-title">
    <svg viewBox="0 0 36 36"><circle cx="11" cy="11" r="9"/><circle cx="11" cy="11" r="4" fill="#151515"/><path d="M16 15 34 31l-3 3-3-3-2 2-3-3 2-2-9-8z"/></svg>
    <h2>What to look for in a Security Consultant:</h2>
  </div>

  <svg width="0" height="0" style="position:absolute">
    <defs><symbol id="shield" viewBox="0 0 24 28"><path d="M1 2h22v12c0 7-6 11-11 13C7 25 1 21 1 14z" fill="#f2f2f2"/></symbol></defs>
  </svg>

  <div class="abs criterion" style="left:35px;top:522px"><svg><use href="#shield"/></svg><span>A consultant who is Board Certified in Security management</span></div>
  <div class="abs criterion" style="left:219px;top:522px"><svg><use href="#shield"/></svg><span>A consultant who has experience and is considered a expert in corporate security</span></div>
  <div class="abs criterion" style="left:419px;top:522px"><svg><use href="#shield"/></svg><span>A consultant who is Board Certified in Security management</span></div>
  <div class="abs criterion" style="left:606px;top:522px"><svg><use href="#shield"/></svg><span>A consultant who has experience and is considered a expert in corporate security</span></div>
  <div class="abs criterion" style="left:35px;top:642px"><svg><use href="#shield"/></svg><span>A consultant who clearly understands Business and how Security affects the bottom line</span></div>
  <div class="abs criterion" style="left:219px;top:645px"><svg><use href="#shield"/></svg><span>A consultant who is independent who is focused on helping you address your issues.</span></div>
  <div class="abs criterion" style="left:419px;top:645px"><svg><use href="#shield"/></svg><span>A consultant who has worked as a senior manager of a security organization</span></div>

  <div class="abs rule" style="left:27px;top:785px;width:775px"></div>

  <section class="abs cert-copy">
    <h3>Accredited Defense Specialist (ADS)</h3>
    <p>The Accredited Defense Specialist (ADS) is considered the “gold standard” certification for security management professionals and demonstrates knowledge and competency in seven key domains of security. Globally recognized as the standard of excellence for security management professionals. The ADS is administered by OPRA Worldwide, which is the predominant international organization for security Internationally.</p>
  </section>

  <div class="abs cert-badge" role="img" aria-label="Certification badge"></div>

  <h2 class="abs contact-title">CONTACT US:</h2>
  <div class="abs contact-band">
    <span class="contact-item">
      <svg viewBox="0 0 26 26"><rect x="1" y="1" width="24" height="24" rx="5" fill="#111"/><path d="M8 6c1 0 2 3 2 4s-1 1-1 2c1 2 3 4 5 5 1 0 1-1 2-1s4 1 4 2-1 3-3 3C11 21 5 15 5 9c0-2 2-3 3-3z" fill="#c9c9c9"/></svg>
      555-271-6043
    </span>
    <span class="contact-item">
      <svg viewBox="0 0 30 26"><rect x="2" y="4" width="26" height="18" rx="2" fill="none" stroke="#111" stroke-width="2"/><path d="m3 5 12 10L27 5" fill="none" stroke="#111" stroke-width="2"/></svg>
      info@varnelguard.example
    </span>
    <span class="contact-item">
      <svg viewBox="0 0 26 26"><circle cx="13" cy="13" r="12" fill="#111"/><path d="M6 8c3 0 4 2 6 2s1 3-1 4-2 4-4 3-1-4-3-5zm10 5c2 0 4 1 4 3s-2 5-4 5-1-4-2-5 0-3 2-3z" fill="#c9c9c9"/></svg>
      www.varnelguard.example
    </span>
  </div>
</main>
</body>
</html>
```